3月15日にガールズバーをオープン致しました。
ビルの入り口に置いて使うA1立て看板の製作をお願いします。
A4など縮小サイズでもいただけると助かります。
白を基調とした夜でも目立つ感じにしたいです。

セット料金 40分2000円 tax&service 20%

チャージのみ1時間1500円 tax&service 15

クレジットチャージ 10%
飲み放題付き (焼酎 ウイスキー カクテルなど)
ビル3階 席数17席  団体客歓迎

若いギャル系の女の子の写真を大きく入れて頂きたいのですが素材が無く
困ってます。素材をお持ちかたにお願いしたいと思ってます。

現在の看板を添付致しました。ご参考までに。
文章は記載しないでも大丈夫です。

店舗名 Sunflower(サンフラワー)です。

よろしくお願いします。
資料を再添付致しました。よろしくお願いします。
依頼金額を25000円に変更して、延長しました。
提案下さった皆様ありがとうございます。
もう少し提案を見させていただけたらと思います。

具体的なイメージをデザベース様の過去の事例で近いものを添付致しました。
よろしくお願いします。

最初に思い描いてたイメージより良かったです
女の子と背景のピンクもかわいいくて満足です。

ありがとうございました!

提案くださった皆様ありがとうございます!
修正をしてくださった皆様も早急な対応に感謝致します。

ありがとうございました!

```html
<!DOCTYPE html>
<html lang="ja">
<head>
<meta charset="utf-8">
<title>Sunflower ガールズバー</title>
<link rel="stylesheet" href="https://fonts.googleapis.com/css2?family=M+PLUS+Rounded+1c:wght@500;800&family=Noto+Sans+JP:wght@400;700;900&display=swap">
<style>
:root{
  --pink:#e8559b;
  --pink-deep:#d63c86;
  --pink-mid:#ec8dbb;
  --pink-soft:#f7c3dc;
  --pink-pale:#fbe3ef;
  --ink:#3b3438;
  --grey:#5a5357;
  --white:#ffffff;
}
*{margin:0;padding:0;box-sizing:border-box}
html,body{width:846px;height:1200px;overflow:hidden;background:var(--white)}
body{font-family:"Noto Sans JP",sans-serif;color:var(--ink)}
.board{position:relative;width:846px;height:1200px;overflow:hidden;
  background:linear-gradient(180deg,var(--pink-pale) 0%,var(--white) 28%,var(--white) 70%,var(--pink-pale) 100%);
  border:6px solid var(--pink-soft)}
.hero-photo{position:absolute;left:0;top:0;width:410px;height:390px;
  background:radial-gradient(ellipse at 45% 40%,#e9c9b8 0%,#d9b3a0 35%,#f3dbe4 70%,rgba(255,255,255,0) 100%)}
.brand-mark{position:absolute;left:40px;top:330px;width:200px;height:150px;display:flex;flex-direction:column;align-items:center;justify-content:center;gap:8px}
.brand-mark .dot{width:86px;height:86px;border-radius:50%;background:var(--pink-deep)}
.brand-mark .name{font-family:"M PLUS Rounded 1c",sans-serif;font-weight:800;font-size:22px;letter-spacing:2px;color:var(--pink-deep)}
.headline{position:absolute;left:395px;top:14px;width:425px;height:290px;background:var(--white);
  border:4px solid var(--pink-soft);border-radius:24px;padding:16px 0 0 26px;
  font-family:"M PLUS Rounded 1c",sans-serif;font-weight:800;font-size:54px;line-height:1.17;color:var(--pink-deep)}
.headline .deco{position:absolute;right:22px;top:110px;width:105px;height:125px;border-radius:50%;background:radial-gradient(circle,#c94a8a,#f2b6d3)}
.tagline{position:absolute;left:440px;top:325px;font-weight:700;font-size:30px;color:var(--grey)}
.genre{position:absolute;left:395px;top:378px;font-family:"M PLUS Rounded 1c",sans-serif;font-weight:800;font-size:62px;line-height:1.3;color:var(--pink-deep)}
.price-band{position:absolute;left:0;top:480px;width:100%;height:340px;background:linear-gradient(180deg,var(--pink) 0%,var(--pink-mid) 100%)}
.drinks{position:absolute;left:20px;top:500px;color:var(--white);font-weight:900;font-size:44px;white-space:nowrap}
.drinks small{font-size:28px;font-weight:700}
.groups{position:absolute;left:20px;top:562px;font-weight:700;font-size:24px;color:var(--ink)}
.beer{position:absolute;left:30px;top:605px;width:250px;height:190px;border-radius:14px;background:linear-gradient(180deg,#fff6d8 0%,#f2c45a 40%,#e6a52b 100%)}
.label-v{position:absolute;writing-mode:vertical-rl;font-weight:700;font-size:22px;line-height:1;color:var(--pink-deep);letter-spacing:1px;transform:rotate(-18deg)}
.label-set{left:318px;top:560px}
.label-charge{left:318px;top:668px;color:var(--white)}
.price{position:absolute;left:365px;width:465px;height:80px;background:var(--white);border-radius:8px;display:flex;align-items:baseline;justify-content:flex-end;padding-right:18px;color:var(--pink-deep);font-weight:900;font-size:62px;line-height:80px}
.price small{font-size:26px;margin-left:4px}
.price-set{top:555px}
.price-charge{top:685px}
.tax{position:absolute;left:390px;font-weight:700;font-size:32px;color:var(--ink)}
.tax-set{top:638px}
.tax-charge{top:768px}
.store-kicker{position:absolute;left:30px;top:838px;font-weight:700;font-size:28px;color:var(--grey)}
.store-meta{position:absolute;left:395px;top:838px;font-weight:700;font-size:28px;color:var(--grey)}
.store-name{position:absolute;left:22px;top:876px;width:790px;height:130px;border:4px solid var(--pink-soft);border-radius:10px;background:var(--white);
  font-weight:400;font-size:108px;line-height:120px;padding-left:28px;color:var(--grey)}
.hours{position:absolute;left:60px;top:1018px;font-weight:700;font-size:30px;color:var(--pink-deep)}
.credit{position:absolute;left:20px;top:1110px;font-size:22px;line-height:1.4;color:var(--ink)}
.cards{position:absolute;left:395px;top:1105px;display:flex;gap:10px}
.cards span{width:62px;height:40px;border-radius:5px;background:var(--pink-soft);border:1px solid #d9a9c1}
</style>
</head>
<body>
<main class="board">
  <div class="hero-photo" role="img" aria-label="笑顔の若い女性スタッフのポートレート写真"></div>
  <div class="brand-mark"><span class="dot"></span><span class="name">SUNFLOWER</span></div>

  <div class="headline">
    かわいい<br>子たちと<br>気軽に<br>遊べる!!
    <div class="deco" role="img" aria-label="ベリーのイラスト"></div>
  </div>
  <p class="tagline">シックでかわいい</p>
  <h1 class="genre">ガールズバー♪</h1>

  <section class="price-band"></section>
  <p class="drinks">飲み放題！<small>焼酎・ウイスキー・カクテルetc...</small></p>
  <p class="groups">団体客歓迎</p>
  <div class="beer" role="img" aria-label="乾杯するビールグラスのイラスト"></div>

  <span class="label-v label-set">セット料金</span>
  <div class="price price-set">40分2,000<small>円</small></div>
  <p class="tax tax-set">tax&amp;servise20%</p>

  <span class="label-v label-charge">チャージのみ</span>
  <div class="price price-charge">60分1,500<small>円</small></div>
  <p class="tax tax-charge">tax&amp;servise15%</p>

  <p class="store-kicker">GIR'S BEA</p>
  <p class="store-meta">駅前 ビル３F　席数17席</p>
  <h2 class="store-name">Sunflower</h2>
  <p class="hours">Open 20:00~05:00/TEL.03-000-000</p>

  <p class="credit">クレジットOK<br>クレジットチャージ10%</p>
  <div class="cards" aria-label="利用可能なカード">
    <span></span><span></span><span></span><span></span><span></span><span></span>
  </div>
</main>
</body>
</html>
```